MOSLEN Environmental needs an upgrade to its current business cards design

We need an upgrade to our current business cards design, where the MOSLEN acronym is included, as possible and not being overloaded.
MOSLEN Environmental is an Environmental Consultancy Firm based in Sydney.
We would like to see creative designs different from the standard type of business cards (for example, rounded edges, different to standard size of common business cards.

Target Market(s)

industrial companies (oil & gas, petrochemical, mining, insolvency, finance and manufacturing), developers, architect firms, law firms.

Industry/Entity Type

Business

Contact Information for Business Card

logos (brand and acronym), if they don't appear overloaded.
name
role
name of company (MOSLEN Environmental),
address (Level 3, Suite 3C, 47-49 Dorrigan Lane, Wexmoor, NSW, 2188) landline (02 7314 2986)
mobile (staff member)
email (staff member) and
website (www.moslengreen.example).
Include: Contaminated Land, Site Remediation, Groundwater Assessment, Health and Ecological Risk Assessments, Acid Sulfate Soils, Waste Classification.

Font styles to use
Serif
Sans Serif

Requirements
Must have
• A creative design different to the standard type of business cards.
Nice to have
• Rounded edges
• Different size of business cards rather than the standard size.
Should not have
• Preferable not to use white colour background, unless it is required from a creative design proposed.
• Not an overloaded design.
• Avoid black colours

```html
<!DOCTYPE html>
<html lang="en">
<head>
<meta charset="utf-8">
<title>MOSLEN Environmental – Business Card</title>
<link rel="stylesheet" href="https://fonts.googleapis.com/css2?family=Open+Sans:wght@400;600;800&family=Questrial&display=swap">
<style>
  :root {
    --backdrop: #e2e2e0;
    --brand-green: #84c441;
    --card-white: #ffffff;
    --ink-grey: #555759;
    --logo-grey: #5d5e60;
  }
  * { margin: 0; padding: 0; box-sizing: border-box; }
  html, body { width: 1200px; height: 876px; overflow: hidden; }
  body {
    background: var(--backdrop);
    font-family: "Open Sans", Arial, sans-serif;
    position: relative;
  }
  .card {
    position: absolute;
    border-radius: 16px;
  }
  /* Front */
  .card-front {
    left: 184px; top: 241px; width: 394px; height: 392px;
    background: var(--brand-green);
    color: var(--card-white);
  }
  .front-brand {
    position: absolute; left: 0; right: 0; top: 150px;
    text-align: center; font-weight: 800; color: var(--card-white);
  }
  .brand-name { display: block; font-size: 56px; line-height: 56px; letter-spacing: 1px; }
  .brand-sub { display: block; font-size: 15px; letter-spacing: 3px; margin-top: 2px; }
  .services {
    position: absolute; left: 0; right: 0; top: 286px;
    text-align: center; list-style: none;
    font-family: "Questrial", "Century Gothic", sans-serif;
    font-size: 15px; line-height: 21px;
  }
  /* Back */
  .card-back {
    left: 615px; top: 238px; width: 401px; height: 398px;
    background: var(--card-white);
    color: var(--ink-grey);
  }
  .back-brand {
    position: absolute; left: 22px; top: 36px;
    font-weight: 800; color: var(--logo-grey);
  }
  .back-brand .brand-name { font-size: 58px; line-height: 58px; letter-spacing: 1px; }
  .back-brand .brand-sub { font-size: 16px; letter-spacing: 3px; margin-top: 2px; }
  .staff {
    position: absolute; left: 22px; top: 125px;
    font-size: 17px;
  }
  .staff-name { color: var(--brand-green); font-weight: 600; letter-spacing: 0.5px; }
  .address {
    position: absolute; right: 21px; top: 182px;
    text-align: right; font-style: normal;
    font-size: 16.5px; line-height: 21px;
  }
  .address .company { color: var(--brand-green); }
  .contacts {
    position: absolute; right: 22px; top: 277px;
    list-style: none; text-align: right;
    font-size: 16.5px; line-height: 21px;
  }
  .contacts li { display: flex; justify-content: flex-end; align-items: center; gap: 6px; }
  .contacts svg { width: 16px; height: 16px; flex: none; }
</style>
</head>
<body>

<section class="card card-front" aria-label="Card front">
  <div class="front-brand">
    <span class="brand-name">MOSLEN</span>
    <span class="brand-sub">ENVIRONMENTAL</span>
  </div>
  <ul class="services">
    <li>Contaminated Land | Site Remediation</li>
    <li>Groundwater Assessment | Health Risk Assessments</li>
    <li>Acid Sulfate Soils | Waste Classification</li>
  </ul>
</section>

<section class="card card-back" aria-label="Card back">
  <div class="back-brand">
    <span class="brand-name">MOSLEN</span>
    <span class="brand-sub">ENVIRONMENTAL</span>
  </div>
  <p class="staff"><span class="staff-name">COLIN MARWOOD-</span>Project Engineer</p>
  <address class="address">
    <span class="company">MOSLEN Environmental</span><br>
    Level 3, Suite 3C,<br>
    47-49 Dorrigan Lane,<br>
    Wexmoor, NSW, 2188
  </address>
  <ul class="contacts">
    <li>02 7314 2986
      <svg viewBox="0 0 16 16" aria-hidden="true"><rect width="16" height="16" rx="2" fill="#84c441"/><path d="M5 3.5c-.8.4-1.3 1.4-.9 2.7.8 2.8 2.8 5 5.4 6.2 1.2.5 2.2 0 2.7-.8l-1.8-1.6-1.2.7C7.9 10 6.7 8.6 6.2 7.2l.9-1.1L5 3.5z" fill="#fff"/></svg>
    </li>
    <li>staff member
      <svg viewBox="0 0 16 16" aria-hidden="true"><rect x="4" y="1" width="8" height="14" rx="1.5" fill="none" stroke="#84c441" stroke-width="1.4"/><line x1="7" y1="12.5" x2="9" y2="12.5" stroke="#84c441" stroke-width="1.2"/></svg>
    </li>
    <li>staff member
      <svg viewBox="0 0 16 16" aria-hidden="true"><rect x="1" y="3.5" width="14" height="9.5" fill="#84c441"/><path d="M1 3.5l7 5.5 7-5.5" fill="none" stroke="#fff" stroke-width="1.1"/></svg>
    </li>
    <li>www.moslengreen.example
      <svg viewBox="0 0 16 16" aria-hidden="true"><g fill="none" stroke="#84c441" stroke-width="1.1"><circle cx="8" cy="8" r="6.5"/><ellipse cx="8" cy="8" rx="2.8" ry="6.5"/><line x1="1.5" y1="8" x2="14.5" y2="8"/><path d="M2.7 4.8h10.6M2.7 11.2h10.6"/></g></svg>
    </li>
  </ul>
</section>

</body>
</html>
```